Custom Home Builder Website

We need a re-design of a website for our client: "http://www.tovarelbuilds.com". Their current design is outdated and has flash. We need to make it responsive for all devices and with a more professional look.

Pages to consider:
1. Home page
2. Portfolio page - gallery of projects (multiple images of a project with captions, and a main text area for each project).

Good clean design reflecting quality craftsmanship is a must.

We only need designs, no coding required

Target Market(s)

The intended market is home owners looking to build with a reputable and professional home builder.

Industry/Entity Type

Home Builder

Requirements
Must have
• Must Have:
• - main areas of site: home, portfolio, video gallery, contact
Nice to have
• - Maybe pullquotes from testimonials placed as slideshow?

```html
<!DOCTYPE html>
<html lang="en">
<head>
<meta charset="utf-8">
<title>Tovarel Built – Custom Home Builder</title>
<link rel="stylesheet" href="https://fonts.googleapis.com/css2?family=Arimo:ital,wght@0,400;0,700;1,400&family=Cinzel:wght@700&family=Oswald:wght@400&display=swap">
<style>
:root{
  --tan:#c89a66;
  --tan-dark:#b98a57;
  --charcoal:#333333;
  --charcoal-deep:#2b2b2b;
  --text:#555555;
  --muted:#999999;
  --white:#ffffff;
}
*{box-sizing:border-box;margin:0;padding:0}
html,body{width:1174px;height:1200px;overflow:hidden;background:var(--white);font-family:"Arimo",Arial,sans-serif;color:var(--text)}
.page{position:relative;width:1174px;height:1200px}
.abs{position:absolute}

.site-header{position:absolute;left:0;top:0;width:1174px;height:115px;background:linear-gradient(#ffffff,#eeeeee)}
.brand{left:147px;top:36px;font-size:36px;font-weight:700;letter-spacing:3px;color:var(--tan);line-height:1}
.call{left:828px;top:47px;display:flex;gap:14px;align-items:center}
.call-icon{width:36px;height:36px;border-radius:6px;background:var(--charcoal);display:flex;align-items:center;justify-content:center}
.call-label{font-size:13px;color:var(--tan);line-height:1.1}
.call-number{font-size:22px;color:var(--tan);line-height:1.1}

.main-nav{position:absolute;left:0;top:115px;width:1174px;height:42px;background:var(--charcoal);border-top:1px solid #555}
.main-nav ul{position:absolute;left:148px;top:0;display:flex;list-style:none;height:42px;border-left:1px solid #1e1e1e;border-right:1px solid #1e1e1e}
.main-nav li{height:42px;line-height:42px;padding:0 20px;font-size:13px;color:var(--white);border-right:1px solid #1e1e1e}
.main-nav li:last-child{border-right:none}

.hero{position:absolute;left:0;top:157px;width:1174px;height:393px;background:linear-gradient(180deg,#c9bda7 0%,#a58462 45%,#c9ae8b 70%,#b9824f 100%)}
.hero-arrow{position:absolute;top:136px}
.hero-caption{position:absolute;height:35px;line-height:35px;font-size:20px;color:var(--white);padding:0 10px;white-space:nowrap}
.cap-1{left:147px;top:247px;background:rgba(200,154,102,.85)}
.cap-2{left:233px;top:284px;background:rgba(51,51,51,.85)}

.section-title{font-family:"Cinzel",Georgia,serif;font-weight:700;font-size:20px;color:var(--tan);letter-spacing:.5px}
.body-text{font-size:13px;line-height:18.3px;text-align:justify;color:var(--text)}
.body-text p{margin-bottom:18.3px}
.more-link{font-size:11.5px;color:var(--tan);text-transform:uppercase;display:flex;align-items:center;gap:6px}

.tiles{left:599px;top:591px;width:428px;display:grid;grid-template-columns:211px 211px;gap:6px}
.tile-photo{height:117px}
.tile-bar{position:relative;height:28px;background:var(--charcoal);overflow:hidden}
.tile-bar span{position:absolute;left:8px;top:5px;font-family:"Cinzel",Georgia,serif;font-weight:700;font-size:15px;color:var(--white);letter-spacing:.5px}
.tile-bar svg{position:absolute;right:0;top:0}

.news-title{font-size:13px;color:#222;text-transform:uppercase}
.news-date{font-size:11px;font-style:italic;color:var(--muted)}
.quote{font-size:13px;font-style:italic;line-height:16.5px;text-align:justify;color:#333}
.quote-author{font-family:"Oswald",sans-serif;font-size:15px;color:var(--tan);letter-spacing:.5px}
.dot{position:absolute;top:1060px;width:10px;height:10px;border:2px solid var(--tan)}
.dot.active{background:var(--tan)}

.site-footer{position:absolute;left:0;top:1133px;width:1174px;height:67px;background:var(--charcoal-deep)}
.footer-links{left:147px;top:14px;font-size:11px;color:var(--white)}
.footer-links span{margin:0 5px}
.copyright{left:147px;top:37px;font-size:11px;color:var(--white)}
.social{top:17px;width:30px;height:30px;background:var(--white)}
</style>
</head>
<body>
<div class="page">

  <header class="site-header">
    <div class="abs brand">TOVAREL BUILT</div>
    <div class="abs call">
      <div class="call-icon">
        <svg width="20" height="22" viewBox="0 0 20 22"><path d="M5 2c1 0 2 3 2 4s-2 1-2 2 3 6 4 6 1-2 2-2 4 1 4 2-1 4-3 4C6 18 2 10 2 6c0-2 2-4 3-4z" fill="#fff"/></svg>
      </div>
      <div>
        <div class="call-label">CALL US ON</div>
        <div class="call-number">(503) 555-0187</div>
      </div>
    </div>
  </header>

  <nav class="main-nav">
    <ul>
      <li>HOME</li><li>ABOUT US</li><li>SERVICES</li><li>PORTFOLIO</li><li>VIDEO GALLERY</li><li>TOVAREL REWARDS</li><li>NEWS</li><li>CONTACT</li>
    </ul>
  </nav>

  <section class="hero" role="img" aria-label="Open-plan living room with beige sectional sofa, wood kitchen and large windows">
    <svg class="hero-arrow" style="left:62px" width="32" height="76" viewBox="0 0 32 76"><path d="M30 2 4 38l26 36" fill="none" stroke="rgba(255,255,255,.8)" stroke-width="3"/></svg>
    <svg class="hero-arrow" style="left:1072px" width="32" height="76" viewBox="0 0 32 76"><path d="M2 2l26 36L2 74" fill="none" stroke="rgba(255,255,255,.8)" stroke-width="3"/></svg>
    <div class="hero-caption cap-1">LOREM IPSUM DOLOR SIT AMET</div>
    <div class="hero-caption cap-2">CONSECTETUR ADIPISCING ELIT</div>
  </section>

  <h1 class="abs section-title" style="left:149px;top:588px">WELCOME TO TOVAREL BUILT</h1>
  <div class="abs body-text" style="left:147px;top:631px;width:394px">
    <p>Tovarel Custom Homes is a custom home builder and remodeler based in Portland, Oregon- serving the greater Portland Metro area and Central Oregon.  Whether you need a new kitchen or bathroom, a new addition, or you're ready to build your custom dream home, we make the process simple and stress-free.</p>
    <p>With a focus on quality, integrity, sustainability and exceptional project management, our goal is to work with you every step of the way to bring your dreams to reality.  From preliminary design ideas to final clean-up, we take care of all the details.  All you have to do is enjoy watching your project come to life!</p>
    <p style="margin-bottom:0">We look forward to making your dreams a reality!</p>
  </div>
  <div class="abs more-link" style="left:147px;top:880px">
    <svg width="12" height="10" viewBox="0 0 12 10"><path d="M0 5h10M6 1l4 4-4 4" fill="none" stroke="#c89a66" stroke-width="1.5"/></svg>CONTACT US
  </div>

  <div class="abs tiles">
    <div>
      <div class="tile-photo" role="img" aria-label="Bright bedroom with white bed and balcony window" style="background:linear-gradient(#d9d6d2,#b8a48c)"></div>
      <div class="tile-bar"><span>RESIDENTIAL</span><svg width="60" height="28"><polygon points="14,0 60,0 60,28 0,28" fill="#c89a66"/><circle cx="47" cy="14" r="8" fill="none" stroke="#fff" stroke-width="1.5"/><path d="M43 14h7M47 11l3 3-3 3" fill="none" stroke="#fff" stroke-width="1.5"/></svg></div>
    </div>
    <div>
      <div class="tile-photo" role="img" aria-label="Home office with wood cabinetry and desk" style="background:linear-gradient(#b5a68f,#8a5a36)"></div>
      <div class="tile-bar"><span>COMMERCIAL</span><svg width="60" height="28"><polygon points="14,0 60,0 60,28 0,28" fill="#c89a66"/><circle cx="47" cy="14" r="8" fill="none" stroke="#fff" stroke-width="1.5"/><path d="M43 14h7M47 11l3 3-3 3" fill="none" stroke="#fff" stroke-width="1.5"/></svg></div>
    </div>
    <div>
      <div class="tile-photo" role="img" aria-label="New single-storey house exterior under blue sky" style="background:linear-gradient(#8fb2d8,#8c8373 60%,#7a7670)"></div>
      <div class="tile-bar"><span>NEW HOMES</span><svg width="60" height="28"><polygon points="14,0 60,0 60,28 0,28" fill="#c89a66"/><circle cx="47" cy="14" r="8" fill="none" stroke="#fff" stroke-width="1.5"/><path d="M43 14h7M47 11l3 3-3 3" fill="none" stroke="#fff" stroke-width="1.5"/></svg></div>
    </div>
    <div>
      <div class="tile-photo" role="img" aria-label="Kitchen with wood cabinets and grey stone island" style="background:linear-gradient(#8a5633,#6c6a68 65%,#9a6a42)"></div>
      <div class="tile-bar"><span>KITCHENS</span><svg width="60" height="28"><polygon points="14,0 60,0 60,28 0,28" fill="#c89a66"/><circle cx="47" cy="14" r="8" fill="none" stroke="#fff" stroke-width="1.5"/><path d="M43 14h7M47 11l3 3-3 3" fill="none" stroke="#fff" stroke-width="1.5"/></svg></div>
    </div>
  </div>

  <h2 class="abs section-title" style="left:147px;top:932px">TOVAREL NEWS</h2>
  <div class="abs news-title" style="left:148px;top:975px">LOREM IPSUM DOLOR SIT AMET CONSECTETUR.</div>
  <div class="abs news-date" style="left:148px;top:994px">August 27, 2013</div>
  <div class="abs body-text" style="left:148px;top:1018px;width:394px;line-height:16.5px">Lorem ipsum dolor sit amet, consectetur adipiscing elit. Donec at porta odio. Mauris quis nunc nec tellus mattis cursus. Mauris eget purus metus. Pellentesque habitant morbi tristique.</div>
  <div class="abs more-link" style="left:147px;top:1085px">
    <svg width="12" height="10" viewBox="0 0 12 10"><path d="M0 5h10M6 1l4 4-4 4" fill="none" stroke="#c89a66" stroke-width="1.5"/></svg>READ ALL NEWS
  </div>

  <h2 class="abs section-title" style="left:597px;top:932px">TESTIMONIALS</h2>
  <svg class="abs" style="left:599px;top:978px" width="22" height="18" viewBox="0 0 22 18"><path d="M9 2C4 4 2 8 2 12c0 2 1 4 3 4s3-1 3-3-1-3-3-3c0-3 2-5 4-6zM20 2c-5 2-7 6-7 10 0 2 1 4 3 4s3-1 3-3-1-3-3-3c0-3 2-5 4-6z" fill="#333"/></svg>
  <div class="abs quote" style="left:633px;top:974px;width:387px">Lorem ipsum dolor sit amet, consectetur adipiscing elit. Donec at porta odio. Mauris quis nunc nec tellus mattis cursus. Mauris eget purus metus. Pellentesque habitant morbi tristique senectus et netus et malesuada fames ac turpis egestas.</div>
  <div class="abs quote-author" style="left:633px;top:1050px">DANA WHITLOW</div>
  <span class="dot" style="left:980px"></span>
  <span class="dot active" style="left:997px"></span>
  <span class="dot" style="left:1015px"></span>

  <footer class="site-footer">
    <div class="abs footer-links">Home<span>|</span>About Us<span>|</span>Services<span>|</span>Portfolio<span>|</span>Video Gallery<span>|</span>Tovarel Rewards<span>|</span>News<span>|</span>Contact</div>
    <div class="abs copyright">Copyright © 2013 Tovarel Custom Homes. All Rights Reserved.</div>
    <div class="abs social" style="left:958px" aria-label="Social profile"></div>
    <div class="abs social" style="left:997px" aria-label="Social profile"></div>
  </footer>

</div>
</body>
</html>
```